Redesign My Travel Voucher Coupons-Please redesign the flyers I have attached to this brief.

These designs will be catered towards like travel agency vacation stays...luxury resort stays, hotel and airfare getaways, etc. so must have a travel theme but more importantly professional trustworthy appeal...

Please redesign the flyers I have attached to this brief.

I have attached my existing designs. Please use all existing content and elements exactly but make the design much better...also, please keep in mind that these would be full color and printer friendly...

Target Market(s)

Consumers. People receive these vouchers from businesses that run marketing promotions and contests and giveaways. So the look and feel must feel professional and trustworthy but not cheesy and fake.

Industry/Entity Type

Hotel

Requirements
Must have
• Please use all existing content and elements exactly but make the design much better...also, please keep in mind that these would be full color and printer friendly...

MUST HAVE ALL EXISTING CONTENT EXACT NO EXCEPTIONS
Nice to have
• These designs will be catered towards like travel agency vacation stays...luxury resort stays, hotel and airfare getaways, etc. so must have a travel theme but more importantly professional trustworthy appeal...

Should not have

```html
<!DOCTYPE html>
<html lang="en">
<head>
<meta charset="utf-8">
<title>Hotel Stay Certificate</title>
<link rel="stylesheet" href="https://fonts.googleapis.com/css2?family=Poppins:wght@200&family=Questrial&display=swap">
<style>
  :root {
    --paper: #f3f3f3;
    --ink: #2b2b2e;
    --body: #4a4a4e;
    --red: #b8141d;
    --pink: #f2d6de;
    --sky: #cfe1ee;
    --band: #e4e4e4;
    --bubble: #e2e2e2;
    --ticket: #ebebeb;
    --dash: #9a9a9a;
  }
  * { margin: 0; padding: 0; box-sizing: border-box; }
  html, body { width: 1070px; height: 1200px; overflow: hidden; background: var(--paper); }
  body { position: relative; font-family: "Questrial", sans-serif; color: var(--body); }
  .abs { position: absolute; }

  .accent-circle-blue { left: 4px; top: 697px; width: 310px; height: 310px; border-radius: 50%; background: var(--sky); opacity: .75; }
  .accent-circle-pink { left: 995px; top: 294px; width: 150px; height: 122px; border-radius: 61px 0 0 61px; background: var(--pink); }
  .accent-bar-red { left: 1057px; top: 416px; width: 10px; height: 738px; background: var(--red); }
  .side-band { left: 41px; top: 40px; width: 34px; height: 1130px; background: var(--band); }
  .side-photo { left: 75px; top: 55px; width: 114px; height: 1099px;
    background: linear-gradient(180deg, #3b3f66 0%, #7d73b8 22%, #c58fc0 40%, #e6a2a4 52%, #2b2c36 62%, #4b4a55 78%, #6a5f86 90%, #1d1d28 100%); }

  .hero-title { left: 222px; top: 44px; width: 760px; height: 190px; }
  .hero-title text { font-family: "Poppins", sans-serif; font-weight: 200; fill: var(--ink); }
  .offer-banner { left: 227px; top: 228px; width: 752px; height: 35px; background: var(--red); color: #fff;
    font-size: 23px; line-height: 35px; padding-left: 27px; letter-spacing: .2px; }
  .banner-rule { left: 227px; top: 267px; width: 752px; height: 8px; background: var(--band); }

  .section-title { color: var(--red); font-size: 27px; letter-spacing: .4px; text-transform: uppercase; }
  .copy { font-size: 12.6px; line-height: 16.2px; }

  .about { left: 225px; top: 308px; width: 435px; }
  .about .section-title { margin-bottom: 12px; }
  .about p + p { margin-top: 14px; }

  .review { left: 225px; top: 546px; width: 440px; }
  .review .section-title { margin-bottom: 10px; }
  .review-bubble { position: relative; background: var(--bubble); border-radius: 14px; padding: 8px 12px 10px 12px; width: 434px; }
  .review-bubble::after { content: ""; position: absolute; left: 40px; bottom: -14px; border-left: 0 solid transparent;
    border-right: 16px solid transparent; border-top: 14px solid var(--bubble); }
  .review-author { margin-top: 30px; color: var(--red); font-size: 13.5px; font-weight: bold; }

  .features { left: 714px; top: 310px; width: 300px; }
  .features .section-title { margin-bottom: 16px; }
  .feature-list { list-style: none; }
  .feature-list li { position: relative; padding-left: 21px; font-size: 12.6px; line-height: 15px; margin-bottom: 18px; }
  .feature-list svg { position: absolute; left: 0; top: 1px; width: 12px; height: 12px; }

  .destinations { left: 225px; top: 738px; width: 744px; text-align: center; color: var(--red); font-size: 27.5px; line-height: 36px; letter-spacing: .3px; }

  .dashed-rule { left: 224px; width: 745px; border-top: 1px dashed #d49aa0; }
  .recipient { left: 224px; top: 830px; width: 745px; text-align: center; font-size: 26.5px; color: var(--ink); letter-spacing: .6px; }
  .recipient span, .recipient svg { display: inline-block; vertical-align: middle; }
  .recipient svg { margin: 0 28px; width: 30px; height: 16px; }

  .intro { left: 232px; top: 893px; width: 730px; text-align: center; font-size: 13.2px; line-height: 17.5px; }

  .ticket { left: 211px; top: 996px; width: 766px; height: 103px; }
  .ticket-photo { left: 725px; top: 1000px; width: 252px; height: 95px;
    background: linear-gradient(180deg, #6da6d4 0%, #4f7f57 35%, #2f5c34 60%, #2fb5b3 82%, #1b8f96 100%);
    clip-path: polygon(0 0, 94% 0, 100% 8%, 96% 22%, 100% 40%, 100% 100%, 0 100%); }
  .ticket-label { font-size: 12.5px; color: #555; text-transform: uppercase; line-height: 14px; }
  .ticket-value { font-size: 13px; color: var(--red); font-weight: bold; line-height: 15px; }
  .ticket-divider { width: 1px; height: 24px; background: #555; }
  .ticket-url { color: var(--red); font-size: 13.5px; font-weight: bold; letter-spacing: .2px; }
  .ticket-terms { font-size: 9.3px; color: #555; text-transform: uppercase; }

  .compliments { left: 224px; top: 1114px; width: 745px; text-align: center; font-size: 16.5px; color: var(--ink); }
  .compliments span, .compliments svg { display: inline-block; vertical-align: middle; }
  .compliments .lead { text-transform: uppercase; letter-spacing: .5px; }
  .compliments svg { margin: 0 18px; width: 28px; height: 14px; }
</style>
</head>
<body>
  <div class="abs accent-circle-blue"></div>
  <div class="abs accent-circle-pink"></div>
  <div class="abs accent-bar-red"></div>
  <div class="abs side-band"></div>
  <div class="abs side-photo" role="img" aria-label="Palm tree and resort poolside with umbrellas at a pink and purple sunset"></div>

  <svg class="abs hero-title" viewBox="0 0 760 190" aria-label="Enjoy">
    <text x="4" y="168" font-size="226" textLength="752" lengthAdjust="spacingAndGlyphs">ENJOY</text>
  </svg>
  <div class="abs offer-banner">A 2 Night Hotel Stay Of 3+ Star Hotel Accomodations</div>
  <div class="abs banner-rule"></div>

  <section class="abs about">
    <h2 class="section-title">How Can We Do This?</h2>
    <p class="copy">We contract with the world leading hotel chains and resorts to help them fill their otherwise empty rooms. We help fill empty rooms which the hotels, resorts and cruise lines turn into additional revenue from other areas of their property and future bookings.</p>
    <p class="copy">Hotels rarely experience full occupancy, yet they remain open, providing rooms and services at fixed costs. So when hotels give out their rooms by partnering with marketing companies like us, they might miss out on the room fee, but they already didn't have that in the first place, at least now they have the opportunity to gain a customer for their in-house restaurants, room service, their casinos, an extra day stay, future bookings, etc.</p>
  </section>

  <section class="abs review">
    <h2 class="section-title">What Others Say?</h2>
    <blockquote class="review-bubble copy">"Being able to stay right on the strip in Las Vegas was great. I love that we were able to walk around to all the sites and attractions. The fountains at the Bellamar were AMAZING! The Gondola ride at the Lagunetta was very nice. I LOVED the atmosphere and the food. The whole experience was awesome. THANK YOU!"</blockquote>
    <p class="review-author">Marisol T. San Diego, CA</p>
  </section>

  <section class="abs features">
    <h2 class="section-title">Features</h2>
    <ul class="feature-list">
      <li><svg viewBox="0 0 12 12"><circle cx="6" cy="6" r="5" fill="none" stroke="#b8141d" stroke-width="1.3"/><path d="M3.4 6.2 5.3 8 9.8 3.2" fill="none" stroke="#b8141d" stroke-width="1.4"/></svg>Travel 7 Days A Week</li>
      <li><svg viewBox="0 0 12 12"><circle cx="6" cy="6" r="5" fill="none" stroke="#b8141d" stroke-width="1.3"/><path d="M3.4 6.2 5.3 8 9.8 3.2" fill="none" stroke="#b8141d" stroke-width="1.4"/></svg>Your Choice Of Over 50 Luxury<br>Destinations</li>
      <li><svg viewBox="0 0 12 12"><circle cx="6" cy="6" r="5" fill="none" stroke="#b8141d" stroke-width="1.3"/><path d="M3.4 6.2 5.3 8 9.8 3.2" fill="none" stroke="#b8141d" stroke-width="1.4"/></svg>Good For Two Adults &amp; Two Children</li>
      <li><svg viewBox="0 0 12 12"><circle cx="6" cy="6" r="5" fill="none" stroke="#b8141d" stroke-width="1.3"/><path d="M3.4 6.2 5.3 8 9.8 3.2" fill="none" stroke="#b8141d" stroke-width="1.4"/></svg>Pay Just The Taxes &amp; Fees</li>
      <li><svg viewBox="0 0 12 12"><circle cx="6" cy="6" r="5" fill="none" stroke="#b8141d" stroke-width="1.3"/><path d="M3.4 6.2 5.3 8 9.8 3.2" fill="none" stroke="#b8141d" stroke-width="1.4"/></svg>Multiple Travel Date Requests<br>Allowed</li>
      <li><svg viewBox="0 0 12 12"><circle cx="6" cy="6" r="5" fill="none" stroke="#b8141d" stroke-width="1.3"/><path d="M3.4 6.2 5.3 8 9.8 3.2" fill="none" stroke="#b8141d" stroke-width="1.4"/></svg>Fully Transferable To Another Person</li>
      <li><svg viewBox="0 0 12 12"><circle cx="6" cy="6" r="5" fill="none" stroke="#b8141d" stroke-width="1.3"/><path d="M3.4 6.2 5.3 8 9.8 3.2" fill="none" stroke="#b8141d" stroke-width="1.4"/></svg>No Timeshare No Sales Presentation<br>Guaranteed!</li>
      <li><svg viewBox="0 0 12 12"><circle cx="6" cy="6" r="5" fill="none" stroke="#b8141d" stroke-width="1.3"/><path d="M3.4 6.2 5.3 8 9.8 3.2" fill="none" stroke="#b8141d" stroke-width="1.4"/></svg>24 Months To Complete Travel After<br>Redemption</li>
    </ul>
  </section>

  <p class="abs destinations">In The City Of Your Choice Of Over 50<br>Of The Most Popular Destinations Available!</p>

  <div class="abs dashed-rule" style="top:823px"></div>
  <div class="abs recipient">
    <span>EXCLUSIVELY FOR</span>
    <svg viewBox="0 0 30 16"><path d="M2 2l6 6-6 6M11 2l6 6-6 6M20 2l6 6-6 6" fill="none" stroke="#b8141d" stroke-width="1.6"/></svg>
    <span>CARTER ALDWYN</span>
  </div>
  <div class="abs dashed-rule" style="top:874px"></div>

  <p class="abs intro">There is no doubt that everyone wishes they can take a much needed vacation to just relax and unwind while having fun at the same time! Enjoy two nights of hotel accommdations in the city of your choice of over 50 of the hottest, most desired vacation spots around the country. Thanks to the business you received this certificate from, now you can enjoy a nice little mini vacation you deserve!</p>

  <svg class="abs ticket" viewBox="0 0 766 103" aria-hidden="true">
    <path d="M20 4 H756 L762 10 V93 L756 99 H20 L14 93 V70 Q4 66 4 52 Q4 38 14 34 V10 Z" fill="#ebebeb"/>
    <path d="M20 4 H520 M20 99 H520 M14 10 V34 Q4 38 4 52 Q4 66 14 70 V93" fill="none" stroke="#9a9a9a" stroke-width="1.2" stroke-dasharray="4 3"/>
  </svg>
  <div class="abs ticket-photo" role="img" aria-label="Tropical resort pool with thatched cabanas, palms and mountains"></div>

  <div class="abs" style="left:247px;top:1009px">
    <div class="ticket-label">Certificate ID</div>
    <div class="ticket-value">91772-11222</div>
  </div>
  <div class="abs" style="left:247px;top:1051px">
    <div class="ticket-label">Expires</div>
    <div class="ticket-value">10/17/2020</div>
  </div>
  <div class="abs ticket-divider" style="left:345px;top:1011px"></div>
  <div class="abs ticket-divider" style="left:345px;top:1052px"></div>
  <div class="abs" style="left:362px;top:1009px;width:360px">
    <div class="ticket-label">View all the details of this special<br>offer and redeem online at</div>
  </div>
  <div class="abs" style="left:362px;top:1050px;width:360px">
    <div class="ticket-url">WWW.TRAVELPERKSONLINE.COM</div>
    <div class="ticket-terms">*Terms and conditions apply see website for details</div>
  </div>

  <div class="abs compliments">
    <span class="lead">This Certificate Is Compliments Of</span>
    <svg viewBox="0 0 28 14"><path d="M2 2l5 5-5 5M11 2l5 5-5 5M20 2l5 5-5 5" fill="none" stroke="#b8141d" stroke-width="1.6"/></svg>
    <span>Your Company Name Here</span>
  </div>
</body>
</html>
```